Venture Capital firm needs modern business cards

We are a Venture Capital firm within financial services/Asset management. The industry generally has basic business cards with black, blue and maybe green/yellow design elements.
Our firm has a four-colour swoosh logo. We are based in London and want to stand out, just a little bit!, from the crowd. Our company is called ROLK Investments and the 'C' stands for collaboration thus using artfolkhub is a natural portal for our business card design competition. Our logo came via artfolkhub too!
We use 'Venture Partner in Asset Management' as our tagline and this is Trademark registered. We operate in a conservative industry and we should not overstep our mark. The logo is colorful as it is and therefore the rest of the design should not be too fanciful.
The objective is twofold: make our logo element stick and memorable with our audience, whilst representing a conservative yet young image.
The Business Card obviously needs a field for Name, Surname, Job Title, Adress fields: Street, City, Postcode, Country, telefone and cell number, website address, etc.
We have uploaded the ai file. We trust that these are OK. If not, please advise.
Reason: We have have been busy with a client engagement. We will set the project as Guaranteed in return for the troubles we cause. Apologies for the confusion.
Thank you all for these great and creative design suggestions. The team is very happy with a number of your ideas! We will be in touch tomorrow to give individual feedback before the project closes on Friday. We look forward to working with some of you to narrow down your creations. Thank you, ROLK Investments team.
All,
Target Market(s)
Financial Services Professionals, Investors, Media, 35-70 years, mainly male, well educated
Industry/Entity Type
Conservative
Requirements
Must have
- We must make use of our logo and potential tagline 'Venture Partner in Asset Management' as we are establishing a new Brand and new company in the market.
We can use 'ROLK', 'ROLK Investments', and 'ROLK Investments'+tagline 'Venture Partner in Asset Management' or simply the four-colour swoosh plus the name of the company as part of the text. (see files)
All design elements are available in black or grey-scale if required. (grey scale swoosh attached).
Due to regulation we must have the following wording on the card in small print 'ROLK Investments is an Appointed Representative of Brambury Monetary Ventures Limited, which is authorised by the Pemberton Oversight Board'.
Nice to have
- We would consider designs that make use of different printing techniques such embossing/debossing, UV spot etc.
We attach our colour palette in the files section for your reference.
Should not have
- The font we use for our company name is 'EXO' so do not use a font style that clashes with the corporate fonts, please.
Do not use other design elements than the ones we provide in the file library as part of this project.

```html
<!DOCTYPE html>
<html lang="en">
<head>
<meta charset="UTF-8">
<title>ROLK Investments – Business Cards</title>
<link rel="stylesheet" href="https://fonts.googleapis.com/css2?family=Exo:wght@500&family=Arimo:ital,wght@0,400;0,700;1,700&display=swap">
<style>
  :root {
    --stage: #e9e6e1;
    --card-dark: #58585a;
    --card-band: #5c5c5e;
    --card-light: #ffffff;
    --ink: #333436;
    --ink-soft: #7a7a7c;
    --on-dark: #ffffff;
    --on-dark-muted: #b9b9bb;
    --brand-dot: #e8902a;
  }
  * { box-sizing: border-box; margin: 0; padding: 0; }
  html, body { width: 1200px; height: 600px; overflow: hidden; }
  body {
    background: var(--stage);
    position: relative;
    font-family: "Arimo", Arial, sans-serif;
  }
  .card {
    position: absolute;
    box-shadow: 0 6px 14px rgba(0,0,0,.25);
  }

  /* Front card */
  .card-front {
    left: 124px; top: 70px; width: 472px; height: 268px;
    background: var(--card-dark);
  }
  .brand {
    position: absolute;
    display: flex; align-items: center; gap: 14px;
  }
  .brand-mark {
    border-radius: 50%;
    background: var(--brand-dot);
    flex: none;
  }
  .brand-name {
    font-family: "Exo", sans-serif;
    font-weight: 500;
    line-height: 1;
    letter-spacing: 1px;
  }
  .card-front .brand { left: 90px; top: 92px; }
  .card-front .brand-mark { width: 52px; height: 52px; }
  .card-front .brand-name { font-size: 72px; color: var(--on-dark); }
  .tagline {
    position: absolute;
    font-family: "Exo", sans-serif;
    white-space: nowrap;
  }
  .card-front .tagline {
    left: 192px; top: 168px; font-size: 11px; color: var(--on-dark);
  }
  .card-front .website {
    position: absolute; left: 0; right: 0; top: 207px;
    text-align: center;
    font-size: 16px; font-weight: 700; color: var(--on-dark-muted);
  }

  /* Back card */
  .card-back {
    left: 645px; top: 273px; width: 470px; height: 270px;
    background: var(--card-light);
  }
  .card-back .brand { left: 32px; top: 38px; gap: 10px; }
  .card-back .brand-mark { width: 30px; height: 30px; }
  .card-back .brand-name { font-size: 42px; color: var(--ink); }
  .card-back .tagline {
    left: 93px; top: 81px; font-size: 7px; color: var(--ink);
  }
  .person {
    position: absolute; left: 280px; top: 35px;
  }
  .person-name { font-size: 19px; font-weight: 700; color: var(--ink); }
  .person-title {
    font-size: 15px; font-weight: 700; font-style: italic;
    color: var(--ink-soft); margin-top: 1px;
  }
  .address {
    position: absolute; left: 33px; top: 124px;
    font-size: 13px; line-height: 17px; color: var(--ink);
  }
  .contacts {
    position: absolute; left: 282px; top: 116px;
    list-style: none;
    font-size: 12px; line-height: 14.5px; color: var(--ink);
  }
  .contacts b { display: inline-block; width: 13px; }
  .card-band {
    position: absolute; left: 0; right: 0; bottom: 0; height: 80px;
    background: var(--card-band);
    color: var(--on-dark);
    text-align: center;
  }
  .card-band .website {
    margin-top: 10px; font-size: 16px;
  }
  .disclaimer {
    margin-top: 10px; font-size: 11px; line-height: 13px;
  }
</style>
</head>
<body>

  <section class="card card-front">
    <div class="brand">
      <span class="brand-mark"></span>
      <span class="brand-name">ROLK</span>
    </div>
    <p class="tagline">Venture Partner in Asset Management</p>
    <p class="website">www.websitename.com</p>
  </section>

  <section class="card card-back">
    <div class="brand">
      <span class="brand-mark"></span>
      <span class="brand-name">ROLK</span>
    </div>
    <p class="tagline">Venture Partner in Asset Management</p>

    <div class="person">
      <p class="person-name">Name Surname</p>
      <p class="person-title">Job Title</p>
    </div>

    <p class="address">Streetxxxxxx, Cityxxxxxxxx,<br>postcode, Country</p>

    <ul class="contacts">
      <li><b>T</b> 99 9999</li>
      <li><b>M</b> 99 9999</li>
      <li><b>E</b> name@websitename.com</li>
    </ul>

    <div class="card-band">
      <p class="website">www.websitename.com</p>
      <p class="disclaimer">'ROLK Investments is an Appointed Representative of Brambury Monetary Ventures<br>Limited, which is authorised by the Pemberton Oversight Board</p>
    </div>
  </section>

</body>
</html>
```